Marn-ridge Tide Harbor Custom Brokers Limited

Name: Dorvella Hastings
Title: Customs Broker
Address: Shop 9 Birchfield Commercial Complex
207-209 Harlow Road
Kingston 8
Telephone: (876)
Email: tideharborport@quillmail.example

```html
<!DOCTYPE html>
<html lang="en">
<head>
<meta charset="utf-8">
<title>Marn-ridge Tide Harbor Custom Brokers Limited — Business Cards</title>
<link rel="stylesheet" href="https://fonts.googleapis.com/css2?family=Lato:wght@400;700;900&display=swap">
<style>
  :root {
    --navy: #0f1f4f;
    --gold: #e0a526;
    --paper: #f7f7f5;
    --backdrop: #ecebe7;
    --white: #ffffff;
  }
  * { margin: 0; padding: 0; box-sizing: border-box; }
  html, body { width: 1200px; height: 800px; overflow: hidden; }
  body {
    background: var(--backdrop);
    font-family: "Lato", Arial, sans-serif;
    position: relative;
  }
  .card {
    position: absolute;
    width: 540px;
    height: 309px;
    border-radius: 2px;
    box-shadow: 0 10px 28px rgba(0,0,0,0.12);
  }
  .card--front { left: 40px; top: 140px; background: var(--paper); }
  .card--back  { left: 620px; top: 350px; background: var(--navy); }

  .brand {
    position: absolute;
    display: flex;
    align-items: center;
    gap: 10px;
  }
  .brand__dot {
    width: 30px; height: 30px; border-radius: 50%;
    flex: none;
  }
  .brand__name {
    font-weight: 900;
    text-transform: uppercase;
    line-height: 1.15;
    letter-spacing: 0.04em;
  }
  .card--front .brand { right: 34px; top: 40px; }
  .card--front .brand__dot { background: var(--gold); }
  .card--front .brand__name { color: var(--navy); font-size: 15px; }

  .card--back .brand {
    left: 50%; top: 50%;
    transform: translate(-50%, -50%);
  }
  .card--back .brand__dot { background: var(--white); width: 38px; height: 38px; }
  .card--back .brand__name { color: var(--white); font-size: 20px; }

  .divider {
    position: absolute;
    left: 252px; right: 34px; top: 150px;
    height: 1.5px;
    background: var(--gold);
  }
  .holder {
    position: absolute;
    left: 34px; top: 132px;
    color: var(--navy);
  }
  .holder__name {
    font-weight: 900;
    font-size: 22px;
    letter-spacing: 0.03em;
    text-transform: uppercase;
  }
  .holder__title {
    font-size: 13px;
    letter-spacing: 0.08em;
    text-transform: uppercase;
    margin-top: 2px;
  }
  .contact {
    position: absolute;
    left: 34px; top: 206px;
    color: var(--navy);
    font-size: 12.5px;
    line-height: 1.45;
  }
  .contact__address {
    font-weight: 900;
    text-transform: uppercase;
    font-size: 13px;
    letter-spacing: 0.02em;
  }
</style>
</head>
<body>
  <section class="card card--front" aria-label="Business card front">
    <div class="brand">
      <span class="brand__dot"></span>
      <span class="brand__name">Marn-ridge Tide Harbor<br>Custom Brokers Ltd.</span>
    </div>
    <div class="divider"></div>
    <div class="holder">
      <h1 class="holder__name">Dorvella Hastings</h1>
      <p class="holder__title">Customs Broker</p>
    </div>
    <div class="contact">
      <p>Tel. (876)5550 1942</p>
      <p>E-mail. tideharborport@quillmail.example</p>
      <p class="contact__address">Shop 9 Birchfield Commercial Complex</p>
      <p class="contact__address">207-209 Harlow Road, Kingston 8</p>
    </div>
  </section>

  <section class="card card--back" aria-label="Business card back">
    <div class="brand">
      <span class="brand__dot"></span>
      <span class="brand__name">Marn-ridge Tide Harbor<br>Custom Brokers Ltd.</span>
    </div>
  </section>
</body>
</html>
```